International Lifestyle Real Estate Brokerage Needs Eye Catching Website

We need a new website for a cutting edge / dynamic real estate startup, Palmcrest Homes, that will serve as a concierge brokerage to assist cold weather residents with the research, selection, financing and purchase of vacation / retirement properties in warm weather climates in the US and then globally. We will have personally vetted all properties to insure that our clients are only getting the best of the best with no hidden surprises.

** The website design will ultimately need to be coded into a wordpress theme.

We are not locked into any specific colour scheme but would prefer something warm vs cold as that is really the lifestyle we are selling. We like lots of white negative space and hope to allow high end photography to provide most of the pop in colour.

I have attached mock up wire frames to demonstrate desired functionality for three pages we need designed

1) Home Page
2) Market Profile (City overview and developments)
3) Community Profile Page (Individual development profile)

I have also included .ai file for the logo. Not locked into red.

Final design should communicate excitement, lifestyle while maintaining an air of professionalism and reliability. We have developed over 30 sites and have high expectations for the winning design.

Regards,
Dan

Target Market(s)

Canadian and Northern US residents looking to purchase vacation or retirement real estate in warmer climates, initially in the US, but eventually Internationally.

Industry/Entity Type

Real Estate

Contact Information for Business Card

Names for Business Cards

Dan Fairholt
604.555.2716
dan@palmcresthomes.ca

Coding

Coded - Design and coding required

Number of Pages Required

3 page

Font styles to use
Serif
Sans Serif

Requirements
Must have
• See wireframe documents uploaded.
• Site design will ultimately be coded into a child theme to function on a selected wordpress theme. If the designer has a Wordpres Theme in mind that would be compatible with the design we would appreciate that information.
Nice to have
• See wireframe documents uploaded. Prefer clean, modern site, white negative space, bold photography will add most of the colour and pop.
Should not have
• Anything cartoony or sophmoric.

```html
<!DOCTYPE html>
<html lang="en">
<head>
<meta charset="utf-8">
<title>Palmcrest Homes</title>
<link href="https://fonts.googleapis.com/css2?family=Teko:wght@400;500;600&family=Open+Sans:wght@400;600;700&display=swap" rel="stylesheet">
<style>
:root{
  --red:#c0272d;
  --red-dark:#a51f25;
  --ink:#2a2a2a;
  --text:#555;
  --muted:#777;
  --light:#f5f5f5;
  --grey:#e9e9e9;
  --footer:#1f1f1f;
  --footer-bottom:#141414;
  --white:#fff;
  --head:'Teko',sans-serif;
  --body:'Open Sans',sans-serif;
}
*{margin:0;padding:0;box-sizing:border-box}
html,body{width:1200px;height:3377px;overflow:hidden}
body{font-family:var(--body);color:var(--text);background:var(--white);position:relative}
.abs{position:absolute}
section,header,footer{position:absolute;left:0;width:1200px}
.heading{font-family:var(--head);font-weight:400;color:var(--ink);text-transform:uppercase;text-align:center;font-size:38px;line-height:1;letter-spacing:.5px}
.btn{position:absolute;display:flex;align-items:center;justify-content:center;font-size:15px;font-weight:600;color:var(--white);text-transform:uppercase}

/* hero */
.hero{top:0;height:615px;overflow:hidden}
.hero-photo{position:absolute;inset:0;background:linear-gradient(180deg,#cfe3f3 0%,#a9c8e2 35%,#7d9fbe 62%,#4d8aa8 80%,#3fb2c6 88%,#d8c7a8 100%)}
.topbar{position:absolute;right:0;top:0;width:536px;height:40px;background:#2c2c2c;display:flex;gap:34px;align-items:center;justify-content:flex-end;padding-right:60px;color:var(--white);font-size:12px;font-weight:600}
.topbar span{display:flex;align-items:center;gap:7px}
.brand{position:absolute;left:99px;top:62px;display:flex;align-items:center;gap:10px}
.brand-dot{width:20px;height:20px;border-radius:50%;background:var(--red)}
.brand-name{font-family:var(--body);font-weight:700;color:var(--red);font-size:24px;letter-spacing:1px}
.mainnav{position:absolute;right:99px;top:80px;display:flex;gap:32px;font-family:var(--head);font-size:21px;color:var(--ink);text-transform:uppercase}
.hero-title{position:absolute;top:282px;width:1200px;text-align:center;font-family:var(--head);font-weight:500;font-size:52px;line-height:1;color:var(--white);text-transform:uppercase;letter-spacing:1px;text-shadow:0 2px 6px rgba(0,0,0,.45)}
.search{position:absolute;left:263px;top:366px;width:665px;height:52px;background:rgba(255,255,255,.35);padding:6px}
.search-input{position:absolute;left:6px;top:6px;width:535px;height:40px;background:var(--white);font-size:13px;color:#555;padding:12px 20px}
.search-btn{left:554px;top:6px;width:105px;height:40px;background:var(--red);font-size:16px}
.dots{position:absolute;display:flex;gap:8px}
.dots i{width:12px;height:12px;border-radius:50%;border:2px solid var(--white)}
.dots i.on{background:var(--white)}

/* welcome */
.welcome{top:615px;height:585px;background:#f7f7f7}
.welcome .heading{position:absolute;top:66px;width:100%}
.intro{position:absolute;left:162px;top:120px;width:878px;text-align:center;font-size:12px;line-height:22px;color:var(--muted)}
.pillar{position:absolute;top:213px;width:320px;text-align:center}
.pillar-icon{width:112px;height:112px;margin:0 auto;border-radius:50%;background:var(--red);border:5px solid #fff;box-shadow:0 0 0 3px var(--red);display:flex;align-items:center;justify-content:center}
.pillar h3{font-family:var(--head);font-weight:400;font-size:24px;color:var(--ink);margin-top:26px;line-height:1}
.pillar p{font-size:11px;line-height:20px;color:var(--muted);margin-top:6px;padding:0 12px}
.btn-learn{left:461px;top:475px;width:131px;height:38px;background:var(--red);font-size:14px}
.btn-register{left:606px;top:475px;width:132px;height:38px;background:#2e2e2e;font-size:14px}

/* developments */
.dev-head{top:1200px;height:140px;background:var(--white)}
.dev-head .heading{position:absolute;top:36px;width:100%}
.dev-head p{position:absolute;top:82px;width:100%;text-align:center;font-size:15px;line-height:20px;color:var(--muted)}
.dev{top:1340px;height:524px;background:linear-gradient(135deg,#ececec,#e2e2e2)}
.notch{position:absolute;left:576px;top:0;width:0;height:0;border-left:24px solid transparent;border-right:24px solid transparent;border-top:20px solid var(--white)}
.card{position:absolute;top:76px;width:311px;height:322px;overflow:hidden;box-shadow:0 2px 6px rgba(0,0,0,.15)}
.card-photo{position:absolute;inset:0}
.card-cap{position:absolute;left:0;bottom:0;width:100%;height:92px;background:rgba(20,25,15,.72);text-align:center;color:var(--white);padding-top:14px}
.card-cap h4{font-family:var(--head);font-weight:400;font-size:20px;line-height:1}
.card-cap p{font-size:11px;line-height:18px;margin-top:6px;padding:0 24px}
.dev .dots i{border-color:#999}
.dev .dots i.on{background:var(--red);border-color:var(--red)}

/* markets */
.markets{top:1864px;height:687px;background:var(--white)}
.markets .heading{position:absolute;top:48px;width:100%}
.tabs{position:absolute;left:360px;top:124px;width:480px;height:40px;border-bottom:2px solid #e6e6e6;font-size:14px;font-weight:600;color:var(--ink)}
.tab{position:absolute;top:0;height:40px;display:flex;align-items:center;justify-content:center}
.tab.on{left:0;width:156px;background:var(--red);color:var(--white)}
.tile{position:absolute;width:331px;height:225px;overflow:hidden}
.tile-label{position:absolute;left:0;bottom:0;width:100%;height:38px;background:rgba(0,0,0,.6);color:var(--white);font-weight:700;font-size:15px;display:flex;align-items:center;justify-content:center;text-transform:uppercase}
.tile-promo{background:var(--red);color:var(--white);text-align:center;padding:34px 28px 0}
.tile-promo h4{font-family:var(--head);font-weight:400;font-size:24px;line-height:1}
.tile-promo p{font-size:11px;line-height:19px;margin-top:8px}
.btn-outline{position:relative;display:inline-flex;align-items:center;gap:6px;margin-top:16px;border:1px solid var(--white);padding:6px 12px;font-size:11px;font-weight:600}

/* blog */
.blog{top:2551px;height:477px;background:#f7f7f7}
.blog .heading{position:absolute;top:52px;width:100%}
.post{position:absolute;top:130px;width:311px}
.post-photo{height:149px}
.post h5{font-size:15px;font-weight:400;color:var(--red);margin-top:18px}
.post .meta{font-size:13px;color:var(--ink);margin-top:10px;display:flex;align-items:center;gap:6px}
.post p{font-size:12px;line-height:18px;color:var(--ink);margin-top:10px}

/* footer */
.site-footer{top:3028px;height:295px;background:var(--footer);color:#ddd}
.site-footer h6{position:absolute;top:52px;font-family:var(--head);font-weight:400;font-size:23px;color:var(--white);text-transform:uppercase;line-height:1}
.contact-row{position:absolute;left:99px;display:flex;gap:16px;font-size:13px;line-height:19px;color:#ddd}
.map{position:absolute;left:390px;top:92px;width:261px;height:153px;background:linear-gradient(135deg,#d6d6d6,#bdbdbd);border:4px solid #f0f0f0}
.news-text{position:absolute;left:707px;top:86px;width:240px;font-size:12px;line-height:20px}
.news-input{position:absolute;left:707px;top:137px;width:241px;height:39px;background:var(--white);color:#555;font-size:12px;padding:12px}
.btn-sub{left:707px;top:192px;width:99px;height:40px;background:var(--red);font-size:13px;font-weight:400}
.links{position:absolute;left:1002px;top:94px;list-style:none;font-size:13px;line-height:23.8px;text-transform:uppercase}
.links li:before{content:"";display:inline-block;border-left:5px solid #ddd;border-top:4px solid transparent;border-bottom:4px solid transparent;margin-right:10px}
.links li:first-child{text-transform:none}
.bottombar{top:3323px;height:54px;background:var(--footer-bottom);color:#ccc;font-size:12px}
.bottombar .copy{position:absolute;left:99px;top:19px}
.social{position:absolute;right:99px;top:12px;display:flex;gap:10px}
.social i{width:28px;height:28px;border-radius:50%;background:#e8e8e8}
</style>
</head>
<body>

<header class="hero">
  <div class="hero-photo" role="img" aria-label="Sunny coastal city skyline with high-rise towers above a turquoise bay and sandy beach"></div>
  <div class="topbar">
    <span><svg width="13" height="13" viewBox="0 0 13 13"><path d="M6.5 1v7M3.5 5l3 3 3-3M1 11h11" stroke="#fff" stroke-width="2" fill="none"/></svg>SAVED</span>
    <span><svg width="12" height="13" viewBox="0 0 12 13"><circle cx="6" cy="4" r="3" fill="#fff"/><path d="M0 13c0-4 3-5 6-5s6 1 6 5z" fill="#fff"/></svg>ABOUT</span>
    <span><svg width="14" height="11" viewBox="0 0 14 11"><rect x="1" y="1" width="12" height="9" fill="none" stroke="#fff" stroke-width="1.6"/><path d="M1 1l6 5 6-5" stroke="#fff" stroke-width="1.6" fill="none"/></svg>CONTACT</span>
    <span><svg width="11" height="13" viewBox="0 0 11 13"><rect x="0" y="5" width="11" height="8" fill="#fff"/><path d="M2.5 5V3.5a3 3 0 016 0V5" stroke="#fff" stroke-width="1.8" fill="none"/></svg>LOGIN</span>
  </div>
  <div class="brand"><span class="brand-dot"></span><span class="brand-name">PALMCREST HOMES</span></div>
  <nav class="mainnav"><span>Search</span><span>Our Process</span><span>Resources</span><span>Register</span></nav>
  <h1 class="hero-title">Life is too short to be cold</h1>
  <div class="search">
    <div class="search-input">Where do you want to play in the sunshine?</div>
    <div class="btn search-btn">Let's Go!</div>
  </div>
  <div class="dots" style="left:562px;top:452px"><i class="on"></i><i></i><i></i><i></i></div>
</header>

<section class="welcome">
  <h2 class="heading">Welcome to Palmcrest Homes</h2>
  <p class="intro">Sed ut perspiciatis unde omnis iste natus error sit voluptatem accusantium doloremque laudantium, totam rem aperiam, eaque ipsa quae ab illo inventore veritatis et quasi architecto beatae vitae dicta sunt explicabo. Nemo enim ipsam voluptatem quia voluptas sit aspernatur aut odit aut fugit, sed quia consequuntur magni dolores eos qui ratione voluptatem sequi nesciunt. Neque porro quisquam</p>
  <div class="pillar" style="left:101px">
    <div class="pillar-icon"><svg width="50" height="50" viewBox="0 0 52 52" fill="#fff"><circle cx="20" cy="30" r="11"/><g stroke="#fff" stroke-width="5"><path d="M20 15v30M5 30h30M9 19l22 22M31 19L9 41"/></g><circle cx="20" cy="30" r="4" fill="#c0272d"/><circle cx="38" cy="14" r="7"/><circle cx="38" cy="14" r="2.5" fill="#c0272d"/></svg></div>
    <h3>EDUCATE</h3>
    <p>Sed ut perspiciatis unde omnis iste natus error sit voluptatem accusantium doloremque laudantium, totam rem aperiam, eaque ipsa quae</p>
  </div>
  <div class="pillar" style="left:439px">
    <div class="pillar-icon"><svg width="50" height="50" viewBox="0 0 52 52"><circle cx="26" cy="26" r="18" fill="none" stroke="#fff" stroke-width="10"/><g stroke="#c0272d" stroke-width="4"><path d="M12 12l8 8M40 12l-8 8M12 40l8-8M40 40l-8-8"/></g></svg></div>
    <h3>CURATE</h3>
    <p>Sed ut perspiciatis unde omnis iste natus error sit voluptatem accusantium doloremque laudantium, totam rem aperiam, eaque ipsa quae</p>
  </div>
  <div class="pillar" style="left:779px">
    <div class="pillar-icon"><svg width="48" height="48" viewBox="0 0 50 50" fill="#fff"><path d="M8 14h10a5 5 0 1110 0h10v10a5 5 0 110 10v10H28a5 5 0 10-10 0H8V34a5 5 0 100-10z"/></svg></div>
    <h3>FACILITATE</h3>
    <p>Sed ut perspiciatis unde omnis iste natus error sit voluptatem accusantium doloremque laudantium, totam rem aperiam, eaque ipsa quae</p>
  </div>
  <div class="btn btn-learn">Learn More</div>
  <div class="btn btn-register">Register</div>
</section>

<section class="dev-head">
  <h2 class="heading">Featured Developments</h2>
  <p>Duis aute irure dolor in reprehenderit in voluptate velit esse cillum dolore</p>
</section>
<section class="dev">
  <div class="notch"></div>
  <article class="card" style="left:99px">
    <div class="card-photo" role="img" aria-label="Two-storey green house with white porch under a blue sky" style="background:linear-gradient(180deg,#7fb0dc 0%,#a9c7df 35%,#8a8a6a 60%,#4f6a3a 100%)"></div>
    <div class="card-cap"><h4>DUIS AUTE IRURE DOLOR IN</h4><p>Lorem ipsum dolor sit amet, consectetur adipiscing elit, sed do eiusmod tempor</p></div>
  </article>
  <article class="card" style="left:444px">
    <div class="card-photo" role="img" aria-label="Large family home with gables and a manicured lawn" style="background:linear-gradient(180deg,#6f9fd0 0%,#b8c7d3 35%,#9a8d78 60%,#5c7a3e 100%)"></div>
    <div class="card-cap"><h4>DUIS AUTE IRURE DOLOR IN</h4><p>Lorem ipsum dolor sit amet, consectetur adipiscing elit, sed do eiusmod tempor</p></div>
  </article>
  <article class="card" style="left:786px">
    <div class="card-photo" role="img" aria-label="Stone and stucco home with flowering garden" style="background:linear-gradient(180deg,#5d93cf 0%,#b9c6cf 35%,#a89a84 60%,#4e6a38 100%)"></div>
    <div class="card-cap"><h4>DUIS AUTE IRURE DOLOR IN</h4><p>Lorem ipsum dolor sit amet, consectetur adipiscing elit, sed do eiusmod tempor</p></div>
  </article>
  <div class="dots" style="left:566px;top:453px"><i class="on"></i><i></i><i></i></div>
</section>

<section class="markets">
  <h2 class="heading">Featured Markets</h2>
  <div class="tabs">
    <div class="tab on">UNITED STATES</div>
    <div class="tab" style="left:190px;width:80px">MEXICO</div>
    <div class="tab" style="left:300px;width:160px">SOUTH AMERICA</div>
  </div>
  <div class="tile" style="left:99px;top:178px"><div class="abs" style="inset:0;background:linear-gradient(180deg,#3b5578,#8a7a6a 55%,#4f8fb0)" role="img" aria-label="Modern villa with pool at dusk"></div><div class="tile-label">Orlando</div></div>
  <div class="tile" style="left:434px;top:178px"><div class="abs" style="inset:0;background:linear-gradient(180deg,#6ea6dc,#9b8570 55%,#5f7a46)" role="img" aria-label="Craftsman style home among trees"></div><div class="tile-label">Naples</div></div>
  <div class="tile" style="left:770px;top:178px"><div class="abs" style="inset:0;background:linear-gradient(180deg,#4d8ed6,#b4b0a6 55%,#5d7d3e)" role="img" aria-label="Suburban house with green lawn"></div><div class="tile-label">Fort Meyers</div></div>
  <div class="tile" style="left:99px;top:406px"><div class="abs" style="inset:0;background:linear-gradient(180deg,#1f2d44,#7a5a3a 55%,#2f5c7a)" role="img" aria-label="Luxury home lit at night beside a pool"></div><div class="tile-label">Clearwater</div></div>
  <div class="tile" style="left:434px;top:406px"><div class="abs" style="inset:0;background:linear-gradient(180deg,#7aa8d8,#8a96a4 50%,#557a3c)" role="img" aria-label="Blue-grey townhouses with white trim"></div><div class="tile-label">Asheville</div></div>
  <div class="tile tile-promo" style="left:770px;top:406px">
    <h4>FEATURED MARKETS</h4>
    <p>Sed ut perspiciatis unde omnis iste natus error sit voluptatem accusantium doloremque laudantium, totam rem aperiam, eaque ipsa quae ab illo inventore veritatis et quasi architecto beatae vitae</p>
    <span class="btn-outline">READ MORE <svg width="11" height="11" viewBox="0 0 11 11"><circle cx="5.5" cy="5.5" r="5.5" fill="#fff"/><path d="M4.5 3l2.5 2.5L4.5 8" stroke="#c0272d" stroke-width="1.5" fill="none"/></svg></span>
  </div>
</section>

<section class="blog">
  <h2 class="heading">Recent Blog</h2>
  <article class="post" style="left:99px">
    <div class="post-photo" role="img" aria-label="Colourful waterfront old town rooftops" style="background:linear-gradient(180deg,#4f86c6,#c98a4e 50%,#3d6e8a)"></div>
    <h5>Nemo enim ipsam voluptatem</h5>
    <div class="meta"><svg width="12" height="12" viewBox="0 0 12 12"><circle cx="6" cy="6" r="5" fill="none" stroke="#2a2a2a" stroke-width="1.5"/><path d="M6 3v3h2.5" stroke="#2a2a2a" stroke-width="1.5" fill="none"/></svg>3 minutes ago, 0 comments</div>
    <p>Lorem ipsum dolor sit amet, consectetur adipiscing elit, sed do eiusmod tempor incididunt ut labore et dolore</p>
  </article>
  <article class="post" style="left:450px">
    <div class="post-photo" role="img" aria-label="Harbour city skyline across blue water" style="background:linear-gradient(180deg,#5b9ad8,#8ea3b6 55%,#2f6f9a)"></div>
    <h5>Nemo enim ipsam voluptatem</h5>
    <div class="meta"><svg width="12" height="12" viewBox="0 0 12 12"><circle cx="6" cy="6" r="5" fill="none" stroke="#2a2a2a" stroke-width="1.5"/><path d="M6 3v3h2.5" stroke="#2a2a2a" stroke-width="1.5" fill="none"/></svg>3 minutes ago, 0 comments</div>
    <p>Lorem ipsum dolor sit amet, consectetur adipiscing elit, sed do eiusmod tempor incididunt ut labore et dolore</p>
  </article>
  <article class="post" style="left:790px">
    <div class="post-photo" role="img" aria-label="Couple standing in front of a new home" style="background:linear-gradient(180deg,#b8c4cc,#c8b8a4 55%,#6b8a52)"></div>
    <h5>Nemo enim ipsam voluptatem</h5>
    <div class="meta"><svg width="12" height="12" viewBox="0 0 12 12"><circle cx="6" cy="6" r="5" fill="none" stroke="#2a2a2a" stroke-width="1.5"/><path d="M6 3v3h2.5" stroke="#2a2a2a" stroke-width="1.5" fill="none"/></svg>3 minutes ago, 0 comments</div>
    <p>Lorem ipsum dolor sit amet, consectetur adipiscing elit, sed do eiusmod tempor incididunt ut labore et dolore</p>
  </article>
</section>

<footer class="site-footer">
  <h6 style="left:99px">Contact Us</h6>
  <div class="contact-row" style="top:94px"><svg width="14" height="18" viewBox="0 0 14 18"><path d="M7 17s6-6.5 6-10.5A6 6 0 001 6.5C1 10.5 7 17 7 17z" fill="none" stroke="#ddd" stroke-width="1.5"/><circle cx="7" cy="6.5" r="2" fill="#ddd"/></svg><span>Palmcrest Homes, Suite 4|28 Harbour<br>Lane|Westmere Bay<br>WA 6012</span></div>
  <div class="contact-row" style="top:168px"><svg width="14" height="14" viewBox="0 0 14 14"><path d="M3 1l2.5 3-1.5 1.5c1 2 2.5 3.5 4.5 4.5L10 8.5l3 2.5-1.5 2C7 13 1 7 1 2.5z" fill="none" stroke="#ddd" stroke-width="1.3"/></svg><span>Phone : 1300 555 842</span></div>
  <div class="contact-row" style="top:204px"><svg width="15" height="12" viewBox="0 0 15 12"><rect x="1" y="1" width="13" height="10" fill="none" stroke="#ddd" stroke-width="1.3"/><path d="M1 1l6.5 5L14 1" stroke="#ddd" stroke-width="1.3" fill="none"/></svg><span>support@palmcresthomes.com</span></div>
  <h6 style="left:390px">Our Location</h6>
  <div class="map" role="img" aria-label="Street map showing the office location"></div>
  <h6 style="left:707px">Join Our Newsletter</h6>
  <p class="news-text">Excepteur sint occaecat cupidatat non proident, sunt in culpa qui</p>
  <div class="news-input">Enter Name</div>
  <div class="btn btn-sub">SUBSCRIBE</div>
  <h6 style="left:1002px">Quick Links</h6>
  <ul class="links"><li>About</li><li>Our Process</li><li>Resources</li><li>Register</li><li>Contact</li><li>Login</li><li>Saved</li></ul>
</footer>
<section class="bottombar">
  <span class="copy">Copyright 2016 | All Rights Reserved - Palmcrest Homes</span>
  <div class="social"><i></i><i></i><i></i><i></i></div>
</section>

</body>
</html>
```